Women's Clothing / Pip & Tansy's
I'd prefer to have the logo centered at the top of the letterhead and have the address, etc. listed on the bottom. Also, I'm not fond of the little icons that indicate address, phone, email, web. Maybe an envelope with just the logo on the front and the return address on the flap? I think they all look really busy with the big logo in the corner and the address on the bottom. It's something I won't use often, so simple is good.
I really like the front of the business card in #4 and the back of the card in purple. More feedback later on the rest. Thanks for all of the options so far!
Cute design, thanks! What would it look like if the back was purple and the logo was white?

```html
<!DOCTYPE html>
<html lang="en">
<head>
<meta charset="utf-8">
<title>Pip &amp; Tansy's — Business Cards</title>
<link href="https://fonts.googleapis.com/css2?family=Arimo:wght@400;700&display=swap" rel="stylesheet">
<style>
  :root {
    --stage: #e9e9ec;
    --card: #ffffff;
    --plum: #8e2f6b;
    --ink: #3a3a3a;
    --rule: #6b6b6b;
    --reverse: #ffffff;
    --shadow: rgba(0,0,0,0.18);
  }
  * { margin: 0; padding: 0; box-sizing: border-box; }
  html, body { width: 1200px; height: 1030px; overflow: hidden; }
  body {
    background: var(--stage);
    font-family: "Arimo", Arial, sans-serif;
    position: relative;
  }
  .card {
    position: absolute;
    width: 466px;
    height: 266px;
    background: var(--card);
    border-radius: 12px;
    box-shadow: 0 6px 18px var(--shadow);
  }
  .card--front { left: 233px; top: 236px; }
  .card--back {
    left: 367px; top: 520px;
    background: var(--plum);
    display: flex; align-items: center; justify-content: center;
  }

  .brand {
    position: absolute;
    left: 30px; top: 0; bottom: 0;
    width: 214px;
    display: flex; align-items: center; justify-content: center; gap: 9px;
  }
  .brand__dot { flex: none; }
  .brand__name {
    color: var(--plum);
    font-weight: 700;
    font-size: 23px;
    white-space: nowrap;
  }
  .divider {
    position: absolute;
    left: 257px; top: 68px;
    width: 1.5px; height: 130px;
    background: var(--rule);
  }
  .contact {
    position: absolute;
    left: 273px; top: 70px;
    color: var(--ink);
    font-size: 10px;
    line-height: 1.35;
  }
  .contact__name { color: var(--plum); font-weight: 700; font-size: 15px; line-height: 1.1; }
  .contact__role { font-size: 10px; margin-bottom: 18px; }
  .contact__address { margin-bottom: 12px; }
  .contact__lines { margin-bottom: 12px; }
  .contact__web { color: var(--plum); font-weight: 700; }

  .back-brand { display: flex; align-items: center; gap: 12px; }
  .back-brand__name { color: var(--reverse); font-weight: 700; font-size: 28px; white-space: nowrap; }
</style>
</head>
<body>
  <section class="card card--front" aria-label="Business card front">
    <div class="brand">
      <svg class="brand__dot" width="22" height="22" viewBox="0 0 22 22" aria-hidden="true"><circle cx="11" cy="11" r="11" fill="var(--plum)"/></svg>
      <span class="brand__name">Pip &amp; Tansy's</span>
    </div>
    <div class="divider"></div>
    <div class="contact">
      <p class="contact__name">Maren Holt</p>
      <p class="contact__role">Proprietor</p>
      <p class="contact__address">482 Linden Avenue<br>Harlow, MN 56210</p>
      <p class="contact__lines">P:&nbsp; 218.555.0147<br>E:&nbsp; corbelwrenx@pipandtansys.com</p>
      <p class="contact__web">www.pipandtansys.com</p>
    </div>
  </section>

  <section class="card card--back" aria-label="Business card back">
    <div class="back-brand">
      <svg width="26" height="26" viewBox="0 0 26 26" aria-hidden="true"><circle cx="13" cy="13" r="13" fill="var(--reverse)"/></svg>
      <span class="back-brand__name">Pip &amp; Tansy's</span>
    </div>
  </section>
</body>
</html>
```